Website 950x200 Header w/ logo

I'm in need of a website header for a new site called DaysofMarco.com

The site is basically a glorified blog for myself to write my thoughts about politics, sports, TV shows, current events, whatever. I have a lot of interests.

The site is going to look very very similar to http://www.quickmakerhub.example/4937261/6-tips-to-hold-the-lead-in-design-work

but instead of having a dynamic header that becomes the picture with each article, its just going to be a static header in which I'd like to have the name of the site (Days of Marco) and some kind of logo, pictures, etc - I'm totally open to anything. The only thing is it needs to have a dark (probably black) background and needs to be 950x200px.

I envision a black background, with gray and white as the primary colors and then some secondary colors potentially, but again I'm open to anything as long as it's on the black background or some kind of charcoal gray or wahtever. On the site the black part will go all the way from the left of the screen to the right no matter what the window size, but I'd like to keep all the content inside of 950x200px

email me marco.pellwin@mailnest.example if you have any questions. Thanks!

Industry/Entity Type

Tv

```html
<!DOCTYPE html>
<html lang="en">
<head>
<meta charset="utf-8">
<title>Days of Marco — Header</title>
<link rel="stylesheet" href="https://fonts.googleapis.com/css2?family=Cinzel:wght@400;600&family=Cinzel+Decorative:wght@400&family=Open+Sans:wght@400&display=swap">
<style>
  :root {
    --sky-white: #ffffff;
    --mist-gray: #dcdcdc;
    --mid-gray: #8e8e8e;
    --deep-gray: #3a3a3a;
    --ink-black: #000000;
    --dot-tone: rgba(20, 20, 20, 0.28);
    --domain-gray: #c4c4c4;
  }
  html, body {
    margin: 0;
    padding: 0;
    width: 1200px;
    height: 333px;
    overflow: hidden;
    background: var(--ink-black);
  }
  .header-canvas {
    position: relative;
    width: 1200px;
    height: 333px;
    overflow: hidden;
    background: linear-gradient(
      to bottom,
      var(--sky-white) 0%,
      var(--sky-white) 8%,
      var(--mist-gray) 18%,
      #b9b9b9 40%,
      var(--mid-gray) 62%,
      var(--deep-gray) 85%,
      var(--ink-black) 100%
    );
  }
  .dot-swirl {
    position: absolute;
    left: 20px;
    top: 80px;
    width: 1170px;
    height: 240px;
    background: radial-gradient(
      ellipse at 50% 55%,
      transparent 0%,
      transparent 38%,
      var(--dot-tone) 62%,
      transparent 80%
    );
  }
  .brand-mark {
    position: absolute;
    left: 48px;
    top: 110px;
    width: 170px;
    margin: 0;
    font-family: "Cinzel", serif;
    font-weight: 600;
    font-size: 30px;
    line-height: 1.05;
    color: var(--ink-black);
  }
  .site-title {
    position: absolute;
    left: 0;
    right: 0;
    top: 158px;
    margin: 0;
    text-align: center;
    font-family: "Cinzel Decorative", "Cinzel", serif;
    font-weight: 400;
    font-size: 50px;
    letter-spacing: 2px;
    color: var(--ink-black);
  }
  .site-domain {
    position: absolute;
    left: 10px;
    top: 250px;
    margin: 0;
    font-family: "Open Sans", sans-serif;
    font-size: 34px;
    font-weight: 400;
    color: var(--domain-gray);
  }
</style>
</head>
<body>
  <header class="header-canvas">
    <div class="dot-swirl" role="img" aria-label="Swirl of scattered dark oval dots across the header"></div>
    <p class="brand-mark">Days of Marco</p>
    <h1 class="site-title">Days of Marco</h1>
    <p class="site-domain">DaysofMarco.com</p>
  </header>
</body>
</html>
```